eMail HTML Marketing Template

I need an HTML e-mail marketing template design based off our current website theme (www.trelvane.com). If you need anymore info or have questions please let me know and I will get back to you ASAP.

Goal: A monthly newsletter template for email marketing. Please use lorem ipsum for content filler. If you need to purchase images for the design please let me know and the price to do so.

Thanks.

***URGENT***
If anyone can provide a well designed mockup by 4:00PM EST today (2/6/13) I will award up to two participation prizes of $20 each to each submitter.

Goal: A monthly newsletter template for email marketing.  Please use lorem ipsum for content filler. If you need to purchase images for the design please let me know and the price to do so.

Thanks.

***URGENT***

```html
<!DOCTYPE html>
<html lang="en">
<head>
<meta charset="utf-8">
<title>Trelvane Newsletter – February 2013</title>
<link rel="stylesheet" href="https://fonts.googleapis.com/css2?family=Open+Sans:wght@400;600;700&family=Ubuntu:wght@400;500;700&display=swap">
<style>
  :root {
    --green: #5aa600;
    --black: #000000;
    --white: #ffffff;
    --ink: #1e1e1e;
    --blue: #2b4c8f;
    --blue-light: #3a63b0;
    --heading-blue: #2f4d8c;
    --rule: #d4d4d4;
    --frame: #d8d8d8;
  }
  * { margin: 0; padding: 0; box-sizing: border-box; }
  html, body { width: 1200px; height: 2240px; overflow: hidden; background: var(--white); }
  .canvas { width: 1200px; height: 2240px; position: relative; overflow: hidden; background: var(--white); }
  .newsletter {
    position: absolute; left: 0; top: 0;
    width: 640px; height: 1195px;
    transform: scale(1.875); transform-origin: 0 0;
    font-family: "Ubuntu", "Trebuchet MS", sans-serif;
  }
  .abs { position: absolute; }
  h1, h2 { font-weight: 400; }

  /* Masthead */
  .hero-photo { left: 268px; top: 0; width: 267px; height: 245px;
    background: linear-gradient(135deg, #f3f0e8 0%, #e9c7d0 35%, #9a6fd0 60%, #3a7ed6 100%); }
  .masthead-tab { left: 39px; top: 0; width: 229px; height: 200px; }
  .brand { left: 39px; top: 82px; width: 229px; display: flex; align-items: center; justify-content: center; gap: 8px; }
  .brand-dot { width: 20px; height: 20px; border-radius: 50%; background: var(--green); }
  .brand-name { font-family: "Open Sans", sans-serif; font-weight: 700; font-size: 20px; color: var(--white); letter-spacing: 1px; }
  .issue-date { left: 39px; top: 164px; width: 229px; text-align: center; font-family: "Open Sans", sans-serif; font-size: 14px; color: var(--white); }

  /* Main panel */
  .panel { left: 39px; top: 246px; width: 568px; height: 954px; border-left: 1px solid var(--frame); border-right: 1px solid var(--frame); }
  .intro-bg { left: 39px; top: 246px; width: 568px; height: 310px; }
  .intro-title { left: 39px; top: 266px; width: 568px; text-align: center; font-family: "Open Sans", sans-serif; color: var(--white); line-height: 1; }
  .intro-title .line-1 { display: block; font-size: 30px; }
  .intro-title .line-2 { display: block; font-size: 22px; margin-top: 4px; }
  .intro-copy { left: 74px; top: 381px; width: 500px; color: var(--white); font-size: 10px; font-weight: 700; line-height: 19.5px; }

  .cta-banner { left: 39px; top: 500px; width: 260px; height: 56px; }
  .cta-icon { left: 48px; top: 476px; width: 56px; height: 68px; border-radius: 4px;
    background: linear-gradient(160deg, #ffd640, #f0a000); }
  .cta-label { left: 120px; top: 516px; font-family: "Open Sans", sans-serif; font-size: 17px; color: var(--white); }

  /* Deal columns */
  .deal-photo-left { left: 55px; top: 568px; width: 210px; height: 140px;
    background: linear-gradient(120deg, #e8d8c8, #8fb8e0 45%, #f1d34a 75%, #e7a4c4); }
  .deal-photo-right { left: 330px; top: 568px; width: 228px; height: 132px;
    background: linear-gradient(180deg, #f5f5f5 0%, #f5f5f5 45%, #e2c28a 60%, #e21a1a 80%, #f5f5f5 100%); }
  .deal-tag { top: 709px; width: 257px; height: 44px; }
  .deal-tag.left { left: 39px; }
  .deal-tag.right { left: 349px; }
  .deal-tag-label { top: 722px; font-family: "Open Sans", sans-serif; font-size: 15px; color: var(--white); }
  .deal-copy { top: 767px; width: 240px; font-size: 10px; font-weight: 500; line-height: 18px; color: var(--ink); }
  .col-divider { left: 320px; top: 712px; width: 1px; height: 128px; background: var(--rule); }
  .section-rule { left: 45px; top: 870px; width: 555px; height: 1px; background: var(--rule); }

  /* Feature */
  .feature-art { left: 70px; top: 888px; width: 112px; height: 172px; border-radius: 8px;
    background: linear-gradient(180deg, #f4dcc8 0%, #e8707a 40%, #3a3a3a 70%, #1f1f1f 100%); }
  .feature-title { left: 208px; top: 908px; font-family: "Open Sans", sans-serif; font-size: 19px; color: var(--heading-blue); }
  .feature-copy { left: 210px; top: 948px; width: 396px; font-size: 10px; font-weight: 500; line-height: 17.5px; color: var(--ink); }

  /* Footer */
  .footer-bg { left: 39px; top: 1068px; width: 568px; height: 132px; }
  .social { left: 268px; top: 1084px; display: flex; gap: 8px; }
  .social span { width: 28px; height: 28px; border: 2px solid var(--white); border-radius: 50%; }
  .footer-note { left: 39px; top: 1124px; width: 568px; text-align: center; font-family: "Open Sans", sans-serif; font-size: 11.5px; line-height: 16px; color: var(--white); }
</style>
</head>
<body>
<div class="canvas">
  <div class="newsletter">

    <!-- Masthead -->
    <div class="abs hero-photo" role="img" aria-label="Photo of a smiling woman in sunglasses holding colourful shopping bags"></div>
    <svg class="abs masthead-tab" viewBox="0 0 229 200" aria-hidden="true">
      <rect x="0" y="0" width="229" height="200" fill="var(--green)"/>
      <polygon points="0,0 229,0 229,128 114,152 0,128" fill="var(--black)"/>
    </svg>
    <div class="abs brand"><span class="brand-dot"></span><span class="brand-name">TRELVANE</span></div>
    <div class="abs issue-date">FEBRUARY 2013</div>

    <!-- Main panel -->
    <div class="abs panel"></div>
    <svg class="abs intro-bg" viewBox="0 0 568 310" aria-hidden="true">
      <rect x="0" y="0" width="568" height="310" fill="var(--black)"/>
      <polygon points="0,0 568,0 568,66 284,106 0,66" fill="var(--green)"/>
    </svg>
    <h1 class="abs intro-title"><span class="line-1">GRAB YOUR FREE CUSTOMERS</span><span class="line-2">TODAY!</span></h1>
    <p class="abs intro-copy">This is Trelvane's gift to you as we launch our business. Using our unique social media platform, we will present your business to millions of consumers as we launch. Simply use and activate a Discount Deal or place Items to our MarketPlace to take advantage of this deal. Trelvane will deliver 1...</p>

    <svg class="abs cta-banner" viewBox="0 0 260 56" aria-hidden="true">
      <defs>
        <linearGradient id="ctaBlue" x1="0" y1="0" x2="0" y2="1">
          <stop offset="0" stop-color="var(--blue-light)"/>
          <stop offset="1" stop-color="var(--blue)"/>
        </linearGradient>
      </defs>
      <polygon points="0,0 238,0 260,28 238,56 0,56" fill="url(#ctaBlue)"/>
    </svg>
    <div class="abs cta-icon" role="img" aria-label="Yellow shopping bag with a percent sign"></div>
    <div class="abs cta-label">VIEW THIS FREEBIE!</div>

    <!-- Deal columns -->
    <div class="abs deal-photo-left" role="img" aria-label="Photo of two young women carrying shopping bags"></div>
    <div class="abs deal-photo-right" role="img" aria-label="Photo of a hand holding a clothes hanger with a red sale tag"></div>

    <svg class="abs deal-tag left" viewBox="0 0 257 44" aria-hidden="true">
      <polygon points="0,0 235,0 257,22 235,44 0,44" fill="var(--green)"/>
      <circle cx="22" cy="22" r="10" fill="none" stroke="var(--white)" stroke-width="2.5"/>
      <polyline points="16,22 21,27 30,15" fill="none" stroke="var(--white)" stroke-width="3" stroke-linecap="round" stroke-linejoin="round"/>
    </svg>
    <div class="abs deal-tag-label" style="left:91px">DISCUNT DEALS</div>

    <svg class="abs deal-tag right" viewBox="0 0 257 44" aria-hidden="true">
      <polygon points="0,0 235,0 257,22 235,44 0,44" fill="var(--green)"/>
      <circle cx="29" cy="22" r="10" fill="none" stroke="var(--white)" stroke-width="2.5"/>
      <polyline points="23,22 28,27 37,15" fill="none" stroke="var(--white)" stroke-width="3" stroke-linecap="round" stroke-linejoin="round"/>
    </svg>
    <div class="abs deal-tag-label" style="left:407px">FEATURED DEALS</div>

    <div class="abs col-divider"></div>
    <p class="abs deal-copy" style="left:42px">Lorem Ipsum has been the industry's standard dummy text ever since the 1500s, when an unknown printeley of type and scrambled it to make a type specimen book.</p>
    <p class="abs deal-copy" style="left:351px">Lorem Ipsum has been the industry's standard dummy text ever since the 1500s, when an unknown printeley of type and scrambled it to make a type specimen book.</p>

    <div class="abs section-rule"></div>

    <!-- Feature -->
    <div class="abs feature-art" role="img" aria-label="Woman with shopping bags above a black NEW starburst badge"></div>
    <h2 class="abs feature-title">BETA TEST DISCOUNT DEAL</h2>
    <p class="abs feature-copy">Lorem Ipsum has been the industry's standard dummy text ever since the 1500s, when an unknown printeley of type and scrambled it to make a type specimen book. Lorem Ipsum has been the industry's standard dummy text ever since the 1500s, when an unknown printeley of type and scrambled it to make a type specimen book.</p>

    <!-- Footer -->
    <svg class="abs footer-bg" viewBox="0 0 568 132" aria-hidden="true">
      <polygon points="0,42 284,0 568,42 568,132 0,132" fill="var(--green)"/>
    </svg>
    <div class="abs social" aria-label="Social links"><span></span><span></span><span></span></div>
    <p class="abs footer-note">You are receiving this email as a part of your company's&nbsp; program.<br>Copyright © 2012&nbsp; Trelvane All rights reserved.</p>

  </div>
</div>
</body>
</html>
```